existing Business Card Re design

We are wanting to re design our cards to reflect our new logo , i have attache the current business cards and new logo
i will need a business card that reflects the following information on each card.

card 1:
Harold Dunsby, President
555-382-9164
info@kpqfoamcoat.com

card 2:
Colin Thresher, Outside Sales
Office: 555-382-9164
Cell: 555-617-2048
Sales@kpqfoamcoat.com

Card 3
Louis Varcoe, Branch Manager
Office: 555-382-9164
Cell: 555-493-7752
Louis@kpqfoamcoat.com

Card 4
I will need a Generic card with no name on it just business
555-382-9164
info@kpqfoamcoat.com

Target Market(s)

Homeowners and Contractors

Contact Information for Business Card

We are wanting to re design our cards to reflect our new logo , i have attache the current business cards and new logo. same info on current card

card 1:
Harold Dunsby, President
555-382-9164
info@kpqfoamcoat.com

card 2:
Office: 555-382-9164
Cell: 555-617-2048
Sales@kpqfoamcoat.com

Card 3
Office: 555-382-9164
Cell: 555-493-7752
Louis@kpqfoamcoat.com

Card 4
555-382-9164
info@kpqfoamcoat.com

Requirements
Must have
• same info as current cards with a added business
"sanitizing"

```html
<!DOCTYPE html>
<html lang="en">
<head>
<meta charset="utf-8">
<title>KPQ Foam Coat – Business Card</title>
<link rel="stylesheet" href="https://fonts.googleapis.com/css2?family=Poppins:wght@500;600;700&family=Roboto:wght@400;500&family=Roboto+Condensed:wght@700&display=swap">
<style>
  :root {
    --backdrop: #d9d9d9;
    --white: #ffffff;
    --black: #050505;
    --navy: #0b1626;
    --brand-blue: #1565b8;
    --mid-blue: #1d6fc4;
    --sky-blue: #29a6e1;
    --text-soft: #e8eef6;
  }
  * { box-sizing: border-box; margin: 0; padding: 0; }
  html, body {
    width: 1200px; height: 800px; overflow: hidden;
    background: var(--backdrop);
  }
  .stage { position: relative; width: 1200px; height: 800px; }

  .card {
    position: absolute; top: 283px;
    width: 430px; height: 239px; overflow: hidden;
  }

  /* Front */
  .card-front { left: 111px; background: var(--white); }
  .front-brand {
    position: absolute; top: 0; left: 0; width: 100%; height: 124px;
    display: flex; align-items: center; justify-content: center;
    font-family: "Roboto Condensed", sans-serif; font-weight: 700;
    font-size: 46px; color: var(--brand-blue); letter-spacing: -0.5px;
  }
  .phone-band {
    position: absolute; top: 124px; left: 0; width: 100%; height: 51px;
    background: var(--black);
    display: flex; align-items: center; justify-content: center;
    font-family: "Poppins", sans-serif; font-weight: 700;
    font-size: 44px; color: var(--white); letter-spacing: 1px; line-height: 1;
  }
  .services-band {
    position: absolute; top: 176px; left: 0; width: 100%; height: 28px;
    background: linear-gradient(90deg, var(--black) 0%, var(--black) 55%, var(--mid-blue) 85%, var(--sky-blue) 100%);
    display: flex; align-items: center; justify-content: center;
    font-family: "Poppins", sans-serif; font-weight: 600;
    font-size: 13.5px; color: var(--white); letter-spacing: 0.3px;
  }
  .links-band {
    position: absolute; top: 204px; left: 0; width: 100%; height: 35px;
    background: linear-gradient(90deg, var(--sky-blue) 0%, var(--mid-blue) 38%, var(--black) 62%, var(--black) 100%);
    display: flex; align-items: center; gap: 9px; padding-left: 24px;
    font-family: "Poppins", sans-serif; font-weight: 500;
    font-size: 12.5px; color: var(--white);
  }
  .social-dot {
    width: 16px; height: 16px; border-radius: 50%; background: var(--white);
    flex: none;
  }
  .links-band .web { display: flex; align-items: center; gap: 6px; margin-left: 6px; }

  /* Back */
  .card-back {
    left: 638px;
    background:
      radial-gradient(ellipse 70% 90% at 100% 0%, var(--sky-blue) 0%, rgba(41,166,225,0) 70%),
      linear-gradient(90deg, var(--black) 0%, var(--navy) 22%, #123766 45%, var(--brand-blue) 70%, var(--mid-blue) 100%);
    color: var(--white);
  }
  .holder { position: absolute; left: 26px; top: 28px; font-family: "Poppins", sans-serif; }
  .holder-name { font-size: 13.5px; font-weight: 600; letter-spacing: 0.8px; text-transform: uppercase; }
  .holder-title { font-size: 9.5px; font-weight: 500; letter-spacing: 0.4px; text-transform: uppercase; margin-top: 1px; color: var(--text-soft); }
  .back-brand {
    position: absolute; right: 26px; top: 40px; width: 180px; text-align: right;
    font-family: "Roboto Condensed", sans-serif; font-weight: 700;
    font-size: 34px; line-height: 1.05; color: var(--white);
  }
  .divider { position: absolute; left: 26px; right: 26px; top: 153px; height: 1px; background: rgba(255,255,255,0.85); }
  .contact-list {
    position: absolute; left: 26px; top: 163px; list-style: none;
    font-family: "Roboto", sans-serif; font-size: 9.5px; line-height: 12.6px; color: var(--text-soft);
  }
  .contact-list li { display: flex; align-items: center; gap: 6px; }
  .contact-list svg { width: 8px; height: 8px; flex: none; }
  .address {
    position: absolute; right: 26px; top: 163px; text-align: right;
    font-family: "Roboto", sans-serif; font-size: 9.5px; line-height: 12.6px; color: var(--text-soft);
  }
  .address-line { display: flex; justify-content: flex-end; align-items: center; gap: 6px; }
  .address svg { width: 8px; height: 10px; }
  .address .second { padding-right: 14px; }
</style>
</head>
<body>
<div class="stage">

  <section class="card card-front" aria-label="Business card front">
    <div class="front-brand">KPQ Foam Coat</div>
    <div class="phone-band">555-382-9164</div>
    <div class="services-band">SPRAY FOAM • FIBERGLASS • INSULATION • ROOFING</div>
    <div class="links-band">
      <span class="social-dot" aria-hidden="true"></span>
      <span>kpqfoamcoat</span>
      <span class="web">
        <svg width="16" height="16" viewBox="0 0 16 16" aria-hidden="true" fill="none" stroke="#fff" stroke-width="1.3">
          <circle cx="8" cy="8" r="6.6"/>
          <ellipse cx="8" cy="8" rx="2.8" ry="6.6"/>
          <line x1="1.4" y1="8" x2="14.6" y2="8"/>
          <path d="M2.6 4.6h10.8M2.6 11.4h10.8"/>
        </svg>
        <span>www.kpqfoamcoat</span>
      </span>
    </div>
  </section>

  <section class="card card-back" aria-label="Business card back">
    <div class="holder">
      <div class="holder-name">Colin Thresher</div>
      <div class="holder-title">Outside Sales</div>
    </div>
    <div class="back-brand">KPQ Foam Coat</div>
    <div class="divider"></div>
    <ul class="contact-list">
      <li>
        <svg viewBox="0 0 8 8" aria-hidden="true"><path fill="#e8eef6" d="M0.5 2.2C0.5 1 1.8 0.5 4 0.5S7.5 1 7.5 2.2L6 2.8 5.4 2C5 1.8 3 1.8 2.6 2L2 2.8zM1.5 7.5 2.5 3.6h3l1 3.9z"/></svg>
        555-382-9164
      </li>
      <li>
        <svg viewBox="0 0 8 8" aria-hidden="true"><rect x="2" y="0.4" width="4" height="7.2" rx="0.7" fill="none" stroke="#e8eef6" stroke-width="0.9"/><circle cx="4" cy="6.4" r="0.45" fill="#e8eef6"/></svg>
        555-617-2048
      </li>
      <li>
        <svg viewBox="0 0 8 8" aria-hidden="true"><rect x="0.4" y="1.5" width="7.2" height="5" fill="#e8eef6"/><path d="M0.6 1.8 4 4.6 7.4 1.8" fill="none" stroke="#123766" stroke-width="0.8"/></svg>
        Sales@kpqfoamcoat.com
      </li>
      <li>
        <svg viewBox="0 0 8 8" aria-hidden="true"><circle cx="4" cy="4" r="3.6" fill="#e8eef6"/><path d="M0.5 4h7M4 0.4c-1.6 2-1.6 5.2 0 7.2M4 0.4c1.6 2 1.6 5.2 0 7.2" fill="none" stroke="#123766" stroke-width="0.6"/></svg>
        www.kpqfoamcoat
      </li>
    </ul>
    <div class="address">
      <div class="address-line">
        4820 Larkspur Rd
        <svg viewBox="0 0 8 10" aria-hidden="true"><path fill="#e8eef6" d="M4 0C1.8 0 0.3 1.6 0.3 3.6 0.3 6.2 4 10 4 10S7.7 6.2 7.7 3.6C7.7 1.6 6.2 0 4 0zm0 5.1A1.5 1.5 0 1 1 4 2.1a1.5 1.5 0 0 1 0 3z"/></svg>
      </div>
      <div class="second">Suite 5 Fairview, TX 75069</div>
    </div>
  </section>

</div>
</body>
</html>
```